Bus Bench Ad Design Needed

Hi there. We would like to design an eye catching bus bench ad! The information that we would like to have on it is found below:

- Our logo which is attached below. We would this to take up at least half of the bus bench.
- Our phone number in bold, very visible to see. 555-318-2694. White numbers on an eye catching colored background.
- Our web address : www.SplitEase472.example
- A "Ring Otto" phrase in a black circle with yellow bold letters. Want the "Ring Otto" to be somewhat angled. We are thinking that the "Ring Otto" should be directly below the image in our logo.
- Our tag line we want somewhere in here as well which is "Divorce made easy - at a price you'll like!"

```html
<!DOCTYPE html>
<html lang="en">
<head>
<meta charset="utf-8">
<title>SplitEase Bus Bench Ad</title>
<link href="https://fonts.googleapis.com/css2?family=Anton&family=Jost:wght@400;500&display=swap" rel="stylesheet">
<style>
  :root {
    --stage: #8e8e8e;
    --paper: #ffffff;
    --brand-blue: #0a80c6;
    --sign-yellow: #fdeb2d;
    --ink: #111111;
    --road-light: #c9d98a;
    --road-mid: #6f7a3c;
    --road-dark: #2f3a22;
  }
  * { margin: 0; padding: 0; box-sizing: border-box; }
  html, body {
    width: 1200px; height: 1200px; overflow: hidden;
    background: var(--stage);
  }
  .bench-ad {
    position: absolute; left: 160px; top: 186px;
    width: 915px; height: 820px;
    background: var(--paper);
    font-family: "Jost", Arial, sans-serif;
  }
  .brand {
    position: absolute; left: 84px; top: 62px;
    display: flex; align-items: center;
  }
  .brand-mark {
    width: 96px; height: 96px;
    background: var(--brand-blue);
    margin-right: 46px;
  }
  .brand-divider {
    width: 2px; height: 110px; background: #bbb; margin-right: 14px;
  }
  .brand-text { display: flex; flex-direction: column; }
  .brand-name {
    font-size: 86px; font-weight: 400; line-height: 1;
    color: var(--brand-blue); text-transform: uppercase; letter-spacing: 2px;
  }
  .brand-descriptor {
    font-size: 33px; font-weight: 400; color: #222; line-height: 1.1; margin-top: 4px;
  }
  .phone-band {
    position: absolute; left: 0; top: 259px; width: 100%; height: 137px;
    background: var(--sign-yellow);
  }
  .phone-number {
    position: absolute; left: 314px; top: 12px;
    font-family: "Anton", Impact, sans-serif;
    font-size: 96px; line-height: 1.1; color: var(--ink); letter-spacing: 1px;
  }
  .scenery {
    position: absolute; left: 0; top: 396px; width: 100%; height: 343px;
    background:
      radial-gradient(circle at 8% 28%, rgba(255,255,220,0.85), rgba(255,255,220,0) 30%),
      linear-gradient(180deg, var(--road-light) 0%, #8fa56a 30%, var(--road-mid) 50%, #8a7a5a 75%, var(--road-dark) 100%);
  }
  .tagline {
    position: absolute; left: 0; top: 126px; width: 100%;
    text-align: center; color: #fff;
    font-size: 52px; font-weight: 400; line-height: 68px;
    text-shadow: 3px 3px 0 #111;
  }
  .call-badge {
    position: absolute; left: 45px; top: 217px;
    width: 234px; height: 234px; border-radius: 50%;
    background: var(--ink);
    display: flex; align-items: center; justify-content: center;
  }
  .call-badge span {
    font-family: "Anton", Impact, sans-serif;
    color: var(--sign-yellow); font-size: 62px; line-height: 58px;
    text-align: left; transform: rotate(-8deg); display: block;
  }
  .web-band {
    position: absolute; left: 0; bottom: 0; width: 100%; height: 81px;
    background: var(--brand-blue);
    display: flex; align-items: center; justify-content: center;
  }
  .web-address {
    color: #fff; font-size: 40px; font-weight: 500; letter-spacing: 1px;
  }
</style>
</head>
<body>
  <main class="bench-ad">
    <header class="brand">
      <div class="brand-mark"></div>
      <div class="brand-divider"></div>
      <div class="brand-text">
        <span class="brand-name">SplitEase</span>
        <span class="brand-descriptor">Non-Lawyer Documents Service</span>
      </div>
    </header>

    <section class="phone-band">
      <div class="phone-number">555-318-2694</div>
    </section>

    <section class="scenery" role="img" aria-label="Photo of an open country road stretching toward distant hills under a bright sky with sun flare and trees on both sides">
      <p class="tagline">Divorce made easy<br>- at a price you'll like!</p>
    </section>

    <div class="call-badge"><span>Ring<br>Otto</span></div>

    <footer class="web-band">
      <span class="web-address">www.SplitEase472.example</span>
    </footer>
  </main>
</body>
</html>
```